Book Cover "Venice"

Creation of a cover (14 x 20.5 cm + bleed area) for a book:
Image: “BrumeVerte” (Tiff joined)
AUTHOR: Corinne Valmer
TITLE: The murmurs of Lorient
PUBLISHER: Editions Pluvane (AT THE BOTTOM OF THE COVER)

Target Market(s)

Readers of romantic novels

Industry/Entity Type

Book

```html
<!DOCTYPE html>
<html lang="en">
<head>
<meta charset="utf-8">
<title>The murmurs of Lorient – Book Cover</title>
<link href="https://fonts.googleapis.com/css2?family=Poppins:wght@600;700;800&display=swap" rel="stylesheet">
<style>
  :root {
    --backdrop: #8a3540;
    --sky-top: #4a1a22;
    --sky-red: #d8301e;
    --sky-orange: #f0481f;
    --sky-haze: #a23a3a;
    --city-dark: #1a0707;
    --accent-orange: #f05a28;
    --title-ink: #5a0f12;
  }
  * { margin: 0; padding: 0; box-sizing: border-box; }
  html, body {
    width: 1200px;
    height: 960px;
    overflow: hidden;
    background: var(--backdrop);
  }
  .stage {
    position: relative;
    width: 1200px;
    height: 960px;
    display: flex;
    align-items: center;
    justify-content: center;
  }
  .book-cover {
    position: relative;
    width: 620px;
    height: 908px;
    overflow: hidden;
    font-family: "Poppins", sans-serif;
    box-shadow: 0 10px 30px rgba(0,0,0,0.25);
  }
  .cover-artwork {
    position: absolute;
    inset: 0;
    background:
      linear-gradient(180deg,
        transparent 0%, transparent 62%,
        rgba(26,7,7,0.55) 75%, var(--city-dark) 100%),
      linear-gradient(180deg,
        var(--sky-top) 0%,
        #8a2426 9%,
        var(--sky-red) 18%,
        var(--sky-orange) 30%,
        var(--sky-haze) 42%,
        var(--sky-orange) 52%,
        var(--sky-red) 62%,
        #9a2218 78%,
        var(--city-dark) 100%);
  }
  .cover-author {
    position: absolute;
    top: 52px;
    left: 0;
    right: 0;
    text-align: center;
    font-weight: 700;
    font-size: 32px;
    letter-spacing: 0.5px;
    color: var(--accent-orange);
  }
  .cover-title {
    position: absolute;
    top: 130px;
    left: 72px;
    right: 20px;
    font-weight: 800;
    font-size: 82px;
    line-height: 93px;
    letter-spacing: -1px;
    text-transform: uppercase;
    color: var(--title-ink);
    opacity: 0.85;
    text-shadow: 0 -2px 2px rgba(0,0,0,0.45), 0 2px 1px rgba(255,120,80,0.25);
  }
  .cover-title span { display: block; }
  .cover-publisher {
    position: absolute;
    bottom: 48px;
    left: 0;
    right: 0;
    text-align: center;
    font-weight: 700;
    font-size: 30px;
    color: var(--accent-orange);
  }
</style>
</head>
<body>
  <main class="stage">
    <section class="book-cover">
      <div class="cover-artwork" role="img" aria-label="Painted red sunset sky over a silhouetted harbour town with domes and glowing street lanterns"></div>
      <p class="cover-author">CORINNE VALMER</p>
      <h1 class="cover-title">
        <span>The</span>
        <span>Murmurs</span>
        <span>of</span>
        <span>Lorient</span>
      </h1>
      <p class="cover-publisher">EDITIONS PLUVANE</p>
    </section>
  </main>
</body>
</html>
```